Book Cover for Political Biography

Back round color, darker green.

This book is a political biography of Mr. Ter Haar Veldt who was a prominent politician in Curacao.

Looking for a modern toward the conservative look. The attached images can be used as place holders, we will get hi resolution ones to replace.

Book Title:
Mr. Dr. Anselm ter Haar Veldt: Pionier voor het Bestuurlijke Zelfbeschikking der Westelijke Eilanden

Name Author:
drs. K.J. (Thibault) Wessinghe MBA

Please leave space on the back for book description (one paragraph) and author biography (short paragraph)

```html
<!DOCTYPE html>
<html lang="nl">
<head>
<meta charset="utf-8">
<title>Anselm ter Haar Veldt – Boekomslag</title>
<link rel="stylesheet" href="https://fonts.googleapis.com/css2?family=Libre+Baskerville:ital,wght@0,400;0,700;1,400&display=swap">
<style>
  :root {
    --backdrop: #1f3a2c;
    --backdrop-deep: #142a1f;
    --paper: #ece4d0;
    --paper-light: #f3ecdb;
    --maroon: #7a0f14;
    --maroon-deep: #5e0a0e;
    --band: #9a1a1f;
    --cream-line: #f1e6d0;
    --ink: #2a2522;
    --photo-light: #b9b2a4;
    --photo-dark: #4a463f;
  }
  * { box-sizing: border-box; margin: 0; padding: 0; }
  html, body { width: 1200px; height: 900px; overflow: hidden; }
  body {
    background: radial-gradient(ellipse at 50% 40%, var(--backdrop) 0%, var(--backdrop-deep) 100%);
    font-family: "Libre Baskerville", Georgia, serif;
    position: relative;
  }
  .wrap {
    position: absolute;
    left: 102px; top: 90px;
    width: 996px; height: 720px;
    display: flex;
    box-shadow: 0 14px 34px rgba(0,0,0,.45);
  }

  /* Back cover */
  .back-cover {
    width: 480px; height: 720px;
    background: linear-gradient(180deg, var(--band), var(--maroon-deep));
    color: var(--cream-line);
    display: flex; flex-direction: column;
  }
  .back-section { padding: 38px 40px 0; }
  .back-section.description { height: 360px; }
  .back-section.biography { flex: 1; padding-top: 34px; }
  .back-heading {
    font-size: 15px;
    font-weight: 700;
    letter-spacing: 1.5px;
    text-transform: uppercase;
    margin-bottom: 14px;
  }
  .back-text {
    font-size: 13px;
    line-height: 1.75;
    text-align: justify;
  }
  .back-rule {
    height: 7px;
    border-top: 3px solid var(--cream-line);
    border-bottom: 1px solid var(--cream-line);
  }
  .back-foot { height: 92px; }

  /* Spine */
  .spine {
    width: 36px; height: 720px;
    background: linear-gradient(90deg, var(--maroon-deep), var(--band) 50%, var(--maroon-deep));
    color: var(--cream-line);
    display: flex; flex-direction: column; align-items: center;
    justify-content: space-between;
    padding: 28px 0;
  }
  .spine-title, .spine-author {
    writing-mode: vertical-rl;
    white-space: nowrap;
  }
  .spine-title { font-size: 18px; letter-spacing: 1px; text-transform: uppercase; }
  .spine-author { font-size: 11px; }

  /* Front cover */
  .front-cover {
    width: 480px; height: 720px;
    background: linear-gradient(180deg, var(--paper-light), var(--paper));
    display: flex; flex-direction: column;
  }
  .cover-photo {
    height: 360px;
    background: linear-gradient(135deg, var(--photo-light) 0%, #8c8577 45%, var(--photo-dark) 100%);
  }
  .rule-double {
    height: 7px;
    border-top: 3px solid var(--maroon);
    border-bottom: 1px solid var(--maroon);
  }
  .title-block {
    flex: 1;
    text-align: center;
    padding: 40px 22px 0;
    color: var(--maroon);
  }
  .title-pre {
    display: block;
    font-size: 26px;
    font-weight: 400;
    font-variant: small-caps;
    letter-spacing: 1px;
    line-height: 1;
  }
  .title-main {
    display: block;
    font-size: 38px;
    font-weight: 400;
    text-transform: uppercase;
    letter-spacing: 0.5px;
    line-height: 1.15;
    margin-top: 8px;
  }
  .title-rule {
    width: 414px; height: 2px;
    background: var(--maroon);
    margin: 14px auto 16px;
  }
  .subtitle {
    font-size: 15px;
    line-height: 1.45;
    color: var(--ink);
  }
  .author-band {
    height: 92px;
    background: linear-gradient(180deg, var(--band), var(--maroon-deep));
    border-top: 4px solid var(--maroon);
    box-shadow: inset 0 3px 0 var(--cream-line);
    display: flex; align-items: center; justify-content: center;
    color: var(--cream-line);
    font-size: 14px;
    letter-spacing: .3px;
  }
</style>
</head>
<body>
  <div class="wrap">
    <section class="back-cover">
      <div class="back-section description">
        <h2 class="back-heading">Description</h2>
        <p class="back-text">Lorem ipsum dolor sit amet, consectetur adipiscing elit. Pellentesque habitant morbi tristique senectus et netus. Aliquam erat volutpat. Nulla facilisi, sed tempus elit, at mattis nunc. Vivamus sit amet tellus. Phasellus egestas ante at urna aliquet, quis aliquam libero vehicula. Donec ut nunc commodo.</p>
      </div>
      <div class="back-rule"></div>
      <div class="back-section biography">
        <h2 class="back-heading">Author Biography</h2>
        <p class="back-text">Lorem ipsum dolor sit amet, consectetur adipiscing elit. Pellentesque habitant morbi tristique. Aliquam erat volutpat, sed tempus elit, at mattis nunc tellus. Phasellus egestas ante at urna, quis aliquam libero vehicula commodo.</p>
      </div>
      <div class="back-rule"></div>
      <div class="back-foot"></div>
    </section>

    <div class="spine">
      <span class="spine-title">Ter Haar Veldt</span>
      <span class="spine-author">drs. K.J. (Thibault) Wessinghe MBA</span>
    </div>

    <section class="front-cover">
      <div class="cover-photo" role="img" aria-label="Zwart-witfoto van twee heren in pak aan een gedekte tafel in gesprek"></div>
      <div class="rule-double"></div>
      <div class="title-block">
        <h1>
          <span class="title-pre">Mr. Dr. Anselm</span>
          <span class="title-main">Ter Haar Veldt</span>
        </h1>
        <div class="title-rule"></div>
        <p class="subtitle">Pionier voor het Bestuurlijke Zelfbeschikking<br>der Westelijke Eilanden</p>
      </div>
      <div class="author-band">drs. K.J. (Thibault) Wessinghe MBA</div>
    </section>
  </div>
</body>
</html>
```